Quellbrook Supply Chain and Logistic Consulting

Please review the attached Business Card. I want as close to this card with the colors, fonts, and quality of the card as possible. The attached compass should replace the deer head on both sides of the card and the text should say:

Backside
Compass JPEG
Quellbrook SC&L
A Supply Chain and Logistics Consulting Company

Frontside
Quellbrook SC&L
Ross Pelgrave - Brindle Coast
President
____________________________________
(555) 214-9037
QuellbrookSCL@Mailvento.com
_____________________________________

Bottom Front Side

Target Market(s)

Businesses

Contact Information for Business Card

Backside
Compass JPEG
Quellbrook SC&L

Frontside
Quellbrook SC&L
President
(555) 214-9037
QuellbrookSCL@Mailvento.com

Bottom Front Side

Font styles to use
Serif
Script

Colors

Designer to choose colors to be used in the design.

Requirements
Must have
• See attached card for reference
Nice to have
Should not have

```html
<!DOCTYPE html>
<html lang="en">
<head>
<meta charset="utf-8">
<title>Quellbrook SC&amp;L — Business Card</title>
<link rel="stylesheet" href="https://fonts.googleapis.com/css2?family=Source+Serif+4:wght@400;700&display=swap">
<style>
  :root {
    --card-bg: #000000;
    --text-white: #ffffff;
    --text-silver: #c4c4c4;
    --rule-silver: #bdbdbd;
    --compass-navy: #26344a;
    --compass-deep: #111925;
  }
  * { margin: 0; padding: 0; box-sizing: border-box; }
  html, body {
    width: 1200px;
    height: 691px;
    overflow: hidden;
    background: var(--card-bg);
  }
  .card {
    position: relative;
    width: 1200px;
    height: 691px;
    background: var(--card-bg);
    overflow: hidden;
    font-family: "Source Serif 4", Georgia, serif;
  }
  .compass-art {
    position: absolute;
    left: 897px;
    top: 92px;
    width: 456px;
    height: 456px;
    border-radius: 50%;
    background: radial-gradient(circle at 50% 50%, var(--compass-navy) 0%, var(--compass-deep) 55%, rgba(17,25,37,0.35) 85%, rgba(0,0,0,0) 100%);
  }
  .line {
    position: absolute;
    left: 0;
    width: 1200px;
    text-align: center;
    line-height: 1;
    white-space: nowrap;
  }
  .brand-name {
    top: 87px;
    font-size: 58px;
    font-weight: 700;
    color: var(--text-white);
    letter-spacing: 1px;
  }
  .tagline {
    font-size: 34px;
    font-weight: 400;
    letter-spacing: 1.6px;
  }
  .tagline--top { top: 156px; color: var(--text-silver); }
  .tagline--bottom { top: 592px; color: var(--text-white); }
  .person {
    top: 249px;
    font-size: 32px;
    color: var(--text-white);
    letter-spacing: 1.8px;
  }
  .role {
    top: 302px;
    font-size: 32px;
    color: var(--text-silver);
    letter-spacing: 1.8px;
  }
  .phone, .email {
    font-size: 32px;
    color: var(--text-white);
    letter-spacing: 1.6px;
  }
  .phone { top: 403px; }
  .email { top: 456px; }
  .rules {
    position: absolute;
    inset: 0;
  }
</style>
</head>
<body>
  <div class="card">
    <div class="compass-art" role="img" aria-label="Compass rose illustration, dark navy on black"></div>

    <svg class="rules" width="1200" height="691" viewBox="0 0 1200 691" aria-hidden="true">
      <path d="M318 364.5 Q600 362 883 364.5 Q600 366.5 318 364.5 Z" fill="var(--rule-silver)"/>
      <path d="M318 521.5 Q600 519 883 521.5 Q600 523.5 318 521.5 Z" fill="var(--rule-silver)"/>
      <path d="M64 613 Q119 611.6 174 612 L174 614 Q119 614.4 64 613 Z" fill="var(--rule-silver)"/>
      <path d="M1025 612 Q1080 611.6 1136 613 Q1080 614.4 1025 614 Z" fill="var(--rule-silver)"/>
    </svg>

    <h1 class="line brand-name">Quellbrook SC&amp;L</h1>
    <p class="line tagline tagline--top">A Supply Chain and Logistics Consulting Company</p>
    <p class="line person">Ross Pelgrave - Brindle Coast</p>
    <p class="line role">President</p>
    <p class="line phone">(555) 214-9037</p>
    <p class="line email">QuellbrookSCL@Mailvento.com</p>
    <p class="line tagline tagline--bottom">A Supply Chain and Logistics Consulting Company</p>
  </div>
</body>
</html>
```